Business Consulting Business Card

professional business card with basic information (1) First and Last name (2) email address, (3) phone number, (4) website.

```html
<!DOCTYPE html>
<html lang="en">
<head>
<meta charset="utf-8">
<title>Tidal Reach — Business Card</title>
<link rel="stylesheet" href="https://fonts.googleapis.com/css2?family=Montserrat:wght@300;400;500&display=swap">
<style>
  :root {
    --backdrop: #d2d2cd;
    --card-navy: #062a3f;
    --accent-teal: #4fbdc4;
    --text-light: #e9f1f4;
    --edge-teal: #52c2c4;
  }
  * { margin: 0; padding: 0; box-sizing: border-box; }
  html, body {
    width: 1200px; height: 801px; overflow: hidden;
    background: var(--backdrop);
    font-family: "Montserrat", Arial, sans-serif;
  }
  .stage { position: relative; width: 1200px; height: 801px; }
  .card {
    position: absolute; top: 250px;
    width: 520px; height: 300px;
    background: var(--card-navy);
    border-bottom: 3px solid var(--edge-teal);
  }
  .card--front { left: 60px; }
  .card--back { left: 620px; }

  .brand {
    position: absolute; left: 36px; top: 134px;
    display: flex; align-items: center; gap: 14px;
    white-space: nowrap;
  }
  .brand__dot {
    width: 32px; height: 32px; border-radius: 50%;
    background: var(--accent-teal); flex: none;
  }
  .brand__name {
    color: var(--text-light); font-weight: 300;
    font-size: 21px; letter-spacing: 5px; text-transform: uppercase;
  }
  .divider {
    position: absolute; left: 336px; top: 92px;
    width: 1px; height: 118px; background: var(--accent-teal);
  }
  .contact {
    position: absolute; left: 354px; top: 88px;
    color: var(--text-light); white-space: nowrap;
  }
  .contact__name {
    color: var(--accent-teal); font-weight: 500;
    font-size: 14px; letter-spacing: 0.5px; text-transform: uppercase;
  }
  .contact__role { font-size: 11px; font-weight: 400; margin-top: 2px; }
  .contact__list { list-style: none; margin-top: 14px; }
  .contact__item {
    display: flex; align-items: center; gap: 8px;
    font-size: 11px; font-weight: 400; line-height: 20px;
  }
  .contact__icon { width: 10px; height: 10px; flex: none; }

  .back-mark {
    position: absolute; inset: 0;
    display: flex; align-items: center; justify-content: center;
  }
  .back-mark__dot {
    width: 110px; height: 110px; border-radius: 50%;
    background: var(--accent-teal);
  }
</style>
</head>
<body>
<main class="stage">
  <section class="card card--front" aria-label="Business card front">
    <div class="brand">
      <span class="brand__dot"></span>
      <span class="brand__name">Tidal Reach</span>
    </div>
    <span class="divider"></span>
    <div class="contact">
      <p class="contact__name">Martin Ellery</p>
      <p class="contact__role">Director</p>
      <ul class="contact__list">
        <li class="contact__item">
          <svg class="contact__icon" viewBox="0 0 10 10"><path d="M2 0.8 L3.6 2.6 L2.7 3.6 Q3.8 6 6.4 7.3 L7.4 6.4 L9.2 8 L8 9.3 Q3.5 9 0.7 2 Z" fill="var(--text-light)"/></svg>
          <span>(555) 014-2386</span>
        </li>
        <li class="contact__item">
          <svg class="contact__icon" viewBox="0 0 10 10"><rect x="0.5" y="2" width="9" height="6.5" fill="none" stroke="var(--text-light)"/><path d="M0.5 2 L5 5.6 L9.5 2" fill="none" stroke="var(--text-light)"/></svg>
          <span>hello@tidalreach.co</span>
        </li>
        <li class="contact__item">
          <svg class="contact__icon" viewBox="0 0 10 10"><circle cx="5" cy="5" r="4.4" fill="none" stroke="var(--text-light)"/><ellipse cx="5" cy="5" rx="2" ry="4.4" fill="none" stroke="var(--text-light)"/><path d="M0.6 5 H9.4" stroke="var(--text-light)"/></svg>
          <span>www.tidalreach.co</span>
        </li>
      </ul>
    </div>
  </section>

  <section class="card card--back" aria-label="Business card back">
    <div class="back-mark">
      <span class="back-mark__dot"></span>
    </div>
  </section>
</main>
</body>
</html>
```